Door Company Flyer for October Hardware Sale

We are a door company and need a new flyer for a sale on hardware going on starting today thru the end of October (Oct 1st-Oct 31st) Our logo colors are gray, orange, and white. We need the 3 pictures of hardware included. Our company is TALVO Commercial Door, our supplier is Quorvane and the hardware on sale is Marten brand. We will need this in pdf format to print flyers and also a digital version to post on our website and social media.

```html
<!DOCTYPE html>
<html lang="en">
<head>
<meta charset="utf-8">
<title>TALVO Commercial Door – October Sale Flyer</title>
<link href="https://fonts.googleapis.com/css2?family=Montserrat:wght@300;600;700;800&display=swap" rel="stylesheet">
<style>
  :root {
    --orange: #f7941d;
    --gray: #939598;
    --gray-dark: #58595b;
    --white: #ffffff;
    --backdrop: #333333;
    --ink: #231f20;
  }
  * { box-sizing: border-box; margin: 0; padding: 0; }
  html, body { width: 1200px; height: 1200px; overflow: hidden; }
  body {
    background: var(--backdrop);
    font-family: "Montserrat", Arial, sans-serif;
    position: relative;
  }
  .flyer {
    position: absolute;
    left: 219px; top: 65px;
    width: 762px; height: 1069px;
    background: var(--white);
    box-shadow: 0 4px 14px rgba(0,0,0,.35);
    overflow: hidden;
  }
  .abs { position: absolute; }

  /* brand lockup */
  .brand {
    left: 0; right: 0; top: 40px;
    display: flex; align-items: center; justify-content: center; gap: 16px;
  }
  .brand-mark { width: 54px; height: 90px; background: var(--orange); }
  .brand-name { color: var(--gray); font-weight: 800; line-height: 1; }
  .brand-name .word { display: block; font-size: 66px; letter-spacing: 4px; }
  .brand-name .sub { display: block; font-size: 16.5px; letter-spacing: 1.6px; margin-top: 4px; }

  /* ribbon */
  .ribbon { left: 66px; top: 178px; width: 632px; height: 94px; }
  .ribbon-title {
    left: 114px; top: 178px; width: 536px; height: 72px;
    color: var(--white); font-weight: 700; font-size: 70px;
    line-height: 72px; text-align: center; letter-spacing: .5px;
  }

  .headline {
    left: 0; right: 0; top: 284px; text-align: center;
    color: var(--orange); font-weight: 800; font-size: 51px; line-height: 62px;
    letter-spacing: -.2px; padding-left: 10px;
  }
  .subhead {
    left: 0; right: 0; top: 354px; text-align: center;
    color: var(--gray); font-weight: 800; font-size: 41px; line-height: 48px;
  }
  .dates {
    left: 195px; width: 374px; top: 414px; height: 69px;
    border-top: 3px solid var(--orange); border-bottom: 3px solid var(--orange);
    color: var(--gray); font-weight: 300; font-size: 49px; line-height: 62px;
    text-align: center; white-space: nowrap;
  }

  /* product photo tiles */
  .product { top: 511px; width: 233px; height: 227px; }
  .product-lock { left: 25px; }
  .product-bar  { left: 265px; }
  .product-closer { left: 505px; }

  .brands-heading {
    left: 0; right: 0; top: 754px;
    display: flex; align-items: center; justify-content: center; gap: 18px;
    color: var(--gray); font-weight: 800; font-size: 37px; line-height: 46px;
  }
  .bars { width: 29px; height: 31px; display: flex; flex-direction: column; justify-content: space-between; }
  .bars span { display: block; height: 6px; background: var(--orange); }

  .partner {
    top: 815px; width: 315px; height: 101px;
    border: 1.5px solid var(--gray); display: flex;
  }
  .partner-supplier { left: 48px; }
  .partner-hardware { left: 397px; }
  .partner-role {
    width: 158px; background: var(--gray); color: var(--white);
    font-weight: 700; font-size: 25px;
    display: flex; align-items: center; justify-content: center;
  }
  .partner-name {
    flex: 1; display: flex; align-items: center; justify-content: center;
    color: var(--ink); font-weight: 800; font-size: 26px; letter-spacing: 1px;
  }

  /* footer */
  .footer-rule { left: 0; right: 0; top: 935px; height: 3px; background: var(--orange); }
  .footer { left: 0; right: 0; top: 944px; bottom: 0; background: var(--orange); }
  .cta-tab { left: 116px; top: 944px; width: 525px; height: 40px; }
  .cta {
    left: 116px; width: 525px; top: 944px; height: 40px;
    color: var(--orange); font-weight: 700; font-size: 27px; line-height: 40px; text-align: center;
  }
  .contact {
    left: 23px; right: 23px; top: 1008px; height: 34px;
    display: flex; align-items: center; color: var(--white);
    font-weight: 600; font-size: 20px;
  }
  .contact-item { display: flex; align-items: center; gap: 8px; }
  .contact-phone { margin-right: 28px; }
  .divider { width: 1.5px; height: 34px; background: var(--white); margin: 0 22px 0 24px; }
  .social { display: flex; gap: 10px; }
  .social span { width: 33px; height: 33px; border-radius: 50%; background: var(--white); display: block; }
</style>
</head>
<body>
<main class="flyer">

  <div class="brand abs">
    <span class="brand-mark"></span>
    <div class="brand-name">
      <span class="word">TALVO</span>
      <span class="sub">COMMERCIAL DOOR</span>
    </div>
  </div>

  <svg class="ribbon abs" viewBox="0 0 632 94" aria-hidden="true">
    <polygon points="0,20 48,20 48,72 81,72 81,93 0,93 30,56" fill="#939598"/>
    <polygon points="632,20 584,20 584,72 551,72 551,93 632,93 602,56" fill="#939598"/>
    <rect x="48" y="0" width="536" height="72" fill="#f7941d"/>
  </svg>
  <h1 class="ribbon-title abs">October Sale</h1>

  <h2 class="headline abs">High-Quality Commercial</h2>
  <p class="subhead abs">Doors and Hardware</p>
  <p class="dates abs">Oct 1st-Oct 31st</p>

  <svg class="product product-lock abs" viewBox="0 0 233 227" role="img" aria-label="Photo of a brushed-steel commercial lever lockset">
    <defs>
      <linearGradient id="steel" x1="0" y1="0" x2="1" y2="1">
        <stop offset="0" stop-color="#ffffff"/>
        <stop offset="1" stop-color="#e6e7e8"/>
      </linearGradient>
    </defs>
    <polygon points="37,1 232,1 232,190 195,226 1,226 1,37" fill="url(#steel)" stroke="#939598" stroke-width="1.5"/>
  </svg>
  <svg class="product product-bar abs" viewBox="0 0 233 227" role="img" aria-label="Photo of commercial exit device push bars">
    <polygon points="37,1 232,1 232,190 195,226 1,226 1,37" fill="url(#steel)" stroke="#f7941d" stroke-width="1.5"/>
  </svg>
  <svg class="product product-closer abs" viewBox="0 0 233 227" role="img" aria-label="Photo of an aluminum overhead door closer">
    <polygon points="37,1 232,1 232,190 195,226 1,226 1,37" fill="url(#steel)" stroke="#939598" stroke-width="1.5"/>
  </svg>

  <h3 class="brands-heading abs">
    <span class="bars"><span></span><span></span><span></span></span>
    Notable Brands We Carry
    <span class="bars"><span></span><span></span><span></span></span>
  </h3>

  <div class="partner partner-supplier abs">
    <div class="partner-role">Supplier</div>
    <div class="partner-name">QUORVANE</div>
  </div>
  <div class="partner partner-hardware abs">
    <div class="partner-role">Hardware</div>
    <div class="partner-name">MARTEN</div>
  </div>

  <div class="footer-rule abs"></div>
  <div class="footer abs"></div>
  <svg class="cta-tab abs" viewBox="0 0 525 40" aria-hidden="true">
    <polygon points="0,0 525,0 511,40 14,40" fill="#ffffff"/>
  </svg>
  <p class="cta abs">Contact Us for a Free Estimate</p>

  <div class="contact abs">
    <span class="contact-item contact-phone">
      <svg width="18" height="20" viewBox="0 0 18 20" aria-hidden="true">
        <path d="M4 1 L7 5 L5 8 C6 11 8 13 10 14 L13 12 L17 15 L15 18 C8 18 2 11 2 4 Z" fill="none" stroke="#fff" stroke-width="1.8" stroke-linejoin="round"/>
      </svg>
      (555) 014-2273
    </span>
    <span class="contact-item">
      <svg width="26" height="16" viewBox="0 0 26 16" aria-hidden="true">
        <rect x="1" y="1" width="24" height="14" fill="none" stroke="#fff" stroke-width="1.8"/>
        <path d="M1 1 L13 10 L25 1" fill="none" stroke="#fff" stroke-width="1.8"/>
      </svg>
      sales@talvocommercialdoor.com
    </span>
    <span class="divider"></span>
    <span class="social" aria-label="Social media">
      <span></span><span></span>
    </span>
  </div>

</main>
</body>
</html>
```